Varrow Business Card Design - Professional Flexible and forward thinking. Clean and Easy to follow

Management Consulting Company. I focus on business development and concept and operational review. I need a progressive, simple and professional layout design for the business cards, letterhead and envelops
Professional Flexible and forward thinking. Clean and Easy to follow
Mature Business persons and professionals and Corporations

Target Market(s)

Mature Business persons and professionals and Corporations - Government org.

Industry/Entity Type

Consulting

Contact Information for Business Card

Requirements
Must have
• Marcus Varrow
• President
• Phone - 347.682.1530
• email - Mvarrow@varrowpartners-example.com
• Skype - Marc.varrow
• 2187 Tollbrook Lane
• Suite 4
• Harlow Point, CT 11492
• USA
Nice to have
• www.varrowpartners-example.com
Should not have
• N/A

```html
<!DOCTYPE html>
<html lang="en">
<head>
<meta charset="utf-8">
<title>Varrow Partners Stationery</title>
<link rel="stylesheet" href="https://fonts.googleapis.com/css2?family=Fira+Sans:wght@400;500;600;700&display=swap">
<style>
  :root {
    --orange: #f05a28;
    --orange-light: #f7941d;
    --ink: #231f20;
    --ink-soft: #3a3637;
    --paper: #ffffff;
    --backdrop: #e9e9e7;
    --mist: #f1f1f1;
  }
  * { box-sizing: border-box; margin: 0; padding: 0; }
  html, body { width: 1200px; height: 1200px; overflow: hidden; }
  body {
    background: var(--backdrop);
    font-family: "Fira Sans", Arial, sans-serif;
    color: var(--ink);
    position: relative;
  }
  .sheet { position: absolute; background: var(--paper); box-shadow: 0 2px 6px rgba(0,0,0,.12); overflow: hidden; }

  /* wordmark: invented name, single colour, single weight */
  .wordmark { display: flex; align-items: center; gap: 7px; white-space: nowrap; }
  .wordmark__square { width: 12px; height: 12px; background: var(--orange); flex: none; }
  .wordmark__name { color: var(--ink); font-weight: 500; line-height: 1; }

  /* letterhead */
  .letterhead { left: 60px; top: 110px; width: 480px; height: 640px; }
  .letterhead .wordmark { position: absolute; left: 0; right: 0; top: 48px; justify-content: center; }
  .letterhead .wordmark__name { font-size: 20px; }
  .letterhead__team {
    position: absolute; left: 90px; top: 250px; width: 330px; height: 260px;
    background: linear-gradient(180deg, rgba(235,235,235,.4), var(--mist));
    border-radius: 120px 120px 0 0;
  }
  .letterhead__contact {
    position: absolute; right: 40px; top: 526px; text-align: right;
    font-size: 10px; line-height: 15px; color: var(--ink-soft); white-space: nowrap;
  }
  .letterhead__contact b { font-weight: 600; }
  .letterhead__band {
    position: absolute; left: 0; right: 0; top: 568px; height: 18px;
    background: linear-gradient(90deg, var(--orange), var(--orange-light) 55%, var(--orange));
    font-size: 10px; font-weight: 700; letter-spacing: .12em; color: var(--ink);
    display: flex; align-items: center; justify-content: flex-end; padding-right: 40px; white-space: nowrap;
  }
  .letterhead__rule { position: absolute; left: 0; right: 0; top: 598px; height: 8px; background: var(--orange); }

  /* envelope front */
  .envelope-front { left: 620px; top: 110px; width: 520px; height: 250px; }
  .envelope-front .wordmark { position: absolute; left: 28px; top: 30px; }
  .envelope-front .wordmark__name { font-size: 20px; }
  .envelope-front__address { position: absolute; left: 47px; top: 56px; font-size: 8px; font-weight: 600; color: var(--ink); white-space: nowrap; }
  .envelope-front__band {
    position: absolute; left: 0; right: 0; bottom: 26px; height: 26px;
    background: linear-gradient(90deg, var(--orange), var(--orange-light) 50%, var(--orange));
  }

  /* envelope back */
  .envelope-back { left: 620px; top: 390px; width: 520px; height: 250px; }
  .envelope-back__flap { position: absolute; left: 0; top: 0; }

  /* business cards */
  .card { width: 250px; height: 145px; background: var(--ink); box-shadow: 0 2px 6px rgba(0,0,0,.2); }
  .card-front { left: 620px; top: 680px; }
  .card-front .wordmark { position: absolute; left: 18px; top: 18px; }
  .card-front .wordmark__square { width: 10px; height: 10px; }
  .card-front .wordmark__name { font-size: 14px; color: var(--paper); }
  .card-front__person { position: absolute; left: 18px; top: 80px; }
  .card-front__name { color: var(--orange-light); font-size: 11px; font-weight: 500; white-space: nowrap; }
  .card-front__title { color: #ddd; font-size: 7px; text-align: right; margin-top: 1px; }
  .card-front__details {
    position: absolute; left: 104px; top: 52px; font-size: 5.8px; line-height: 10px; color: #eee;
    border-left: 1px solid var(--orange); padding-left: 6px; white-space: nowrap;
  }
  .card-front__details dt { display: inline; color: var(--orange-light); }
  .card-front__details dd { display: inline; }
  .card-front__band {
    position: absolute; left: 0; right: 0; bottom: 14px; height: 12px; background: var(--orange);
    font-size: 6px; font-weight: 700; color: var(--ink); display: flex; align-items: center; justify-content: center; white-space: nowrap;
  }
  .card-back { left: 890px; top: 680px; }
  .card-back__team {
    position: absolute; left: 70px; top: 16px; width: 110px; height: 70px;
    background: linear-gradient(180deg, #2e2a2b, #3b3738); border-radius: 36px 36px 0 0;
  }
  .card-back__tagline { position: absolute; right: 18px; bottom: 26px; color: var(--paper); font-size: 10px; font-weight: 500; white-space: nowrap; }

  /* logo lockup */
  .lockup { position: absolute; left: 0; right: 0; top: 1005px; display: flex; justify-content: flex-end; padding-right: 120px; }
  .lockup .wordmark { gap: 20px; }
  .lockup .wordmark__square { width: 44px; height: 44px; }
  .lockup .wordmark__name { font-size: 62px; }
</style>
</head>
<body>

  <section class="sheet letterhead" aria-label="Letterhead">
    <div class="wordmark"><span class="wordmark__square"></span><span class="wordmark__name">Varrow Partners</span></div>
    <div class="letterhead__team" role="img" aria-label="Faint group of business professionals in suits"></div>
    <div class="letterhead__contact">
      <p>T: 347.682.1530 | <b>Skype</b> : Marc.varrow</p>
      <p><b>W</b> : www.varrowpartners-example.com | <b>E</b>: Mvarrow@varrowpartners-example.com</p>
    </div>
    <div class="letterhead__band">2187 Tollbrook Lane, Suite 4, Harlow Point, CT 11492, USA</div>
    <div class="letterhead__rule"></div>
  </section>

  <section class="sheet envelope-front" aria-label="Envelope front">
    <div class="wordmark"><span class="wordmark__square"></span><span class="wordmark__name">Varrow Partners</span></div>
    <p class="envelope-front__address">2187 Tollbrook Lane, Suite 4, Harlow Point, CT 11492, USA</p>
    <div class="envelope-front__band"></div>
  </section>

  <section class="sheet envelope-back" aria-label="Envelope back">
    <svg class="envelope-back__flap" width="520" height="80" viewBox="0 0 520 80">
      <path d="M0 0 H520 V30 Q520 52 498 52 H40 Q18 52 10 70 L0 80 Z" fill="var(--orange)"/>
    </svg>
  </section>

  <section class="sheet card card-front" aria-label="Business card front">
    <div class="wordmark"><span class="wordmark__square"></span><span class="wordmark__name">Varrow Partners</span></div>
    <div class="card-front__person">
      <p class="card-front__name">Marcus Varrow</p>
      <p class="card-front__title">President</p>
    </div>
    <dl class="card-front__details">
      <div><dt>Tel : </dt><dd>347.682.1530</dd></div>
      <div><dt>Skype : </dt><dd>Marc.varrow</dd></div>
      <div><dt>Web : </dt><dd>www.varrowpartners-example.com</dd></div>
      <div><dt>Email : </dt><dd>Mvarrow@varrowpartners-example.com</dd></div>
    </dl>
    <div class="card-front__band">2187 Tollbrook Lane, Suite 4, Harlow Point, CT 11492, USA</div>
  </section>

  <section class="sheet card card-back" aria-label="Business card back">
    <div class="card-back__team" role="img" aria-label="Dim group of business professionals in suits"></div>
    <p class="card-back__tagline">Management Consulting Company</p>
  </section>

  <div class="lockup" aria-label="Varrow Partners name">
    <div class="wordmark"><span class="wordmark__square"></span><span class="wordmark__name">Varrow Partners</span></div>
  </div>

</body>
</html>
```